Brochure Design Project

Architectural photography and virtual tour provider for local and national real estate markets. You can use my website for design and image needs. www.larchviewhomeshots.com

```html
<!DOCTYPE html>
<html lang="en">
<head>
<meta charset="utf-8">
<title>Larchview Home Shots – Brochure</title>
<link rel="stylesheet" href="https://fonts.googleapis.com/css2?family=Mulish:ital,wght@0,400;0,700;1,400;1,600&display=swap">
<style>
  :root {
    --page: #ffffff;
    --charcoal: #4a4a4a;
    --charcoal-dark: #454545;
    --fold-line: #5a5a5a;
    --gold: #f0c27a;
    --silver: #bcbcbc;
    --ink: #2e2e2e;
    --brand-green: #5aa657;
    --text-light: #ffffff;
  }
  * { margin: 0; padding: 0; box-sizing: border-box; }
  html, body {
    width: 1200px;
    height: 749px;
    overflow: hidden;
    background: var(--page);
    font-family: "Mulish", "Helvetica Neue", Arial, sans-serif;
  }
  .brochure {
    position: relative;
    width: 1200px;
    height: 749px;
    background: var(--page);
  }
  .brochure__shapes {
    position: absolute;
    inset: 0;
    width: 1200px;
    height: 749px;
  }
  .contact-panel {
    position: absolute;
    left: 365px;
    top: 0;
    width: 332px;
    height: 749px;
    color: var(--text-light);
  }
  .contact-panel__title {
    position: absolute;
    left: 42px;
    top: 49px;
    font-size: 16.5px;
    font-weight: 700;
    letter-spacing: 0.3px;
  }
  .contact-panel__web {
    position: absolute;
    left: 42px;
    top: 88px;
    font-size: 10.5px;
    line-height: 14px;
  }
  .testimonial {
    position: absolute;
    left: 42px;
    top: 283px;
    width: 260px;
  }
  .testimonial__quote {
    font-style: italic;
    font-size: 16px;
    line-height: 20px;
  }
  .testimonial__author {
    margin-top: 11px;
    font-style: italic;
    font-weight: 600;
    font-size: 9.5px;
    line-height: 13px;
  }
  .contact-panel__cta {
    position: absolute;
    left: 0;
    width: 312px;
    top: 684px;
    text-align: center;
    font-style: italic;
    font-weight: 600;
    font-size: 11.5px;
  }
  .brand {
    position: absolute;
    left: 724px;
    top: 531px;
    width: 270px;
  }
  .brand__mark {
    position: absolute;
    left: 6px;
    top: 0;
    width: 30px;
    height: 30px;
    background: var(--brand-green);
  }
  .brand__name {
    position: absolute;
    left: 48px;
    top: 6px;
    font-size: 16px;
    font-weight: 400;
    color: var(--ink);
    white-space: nowrap;
  }
  .brand__former {
    position: absolute;
    left: 69px;
    top: 61px;
    font-size: 9px;
    letter-spacing: 0.4px;
    color: var(--ink);
    white-space: nowrap;
  }
</style>
</head>
<body>
<main class="brochure">
  <svg class="brochure__shapes" viewBox="0 0 1024 630" preserveAspectRatio="none" aria-hidden="false">
    <defs>
      <linearGradient id="interior-tone" x1="0" y1="0" x2="1" y2="1">
        <stop offset="0" stop-color="#eef1f3"/>
        <stop offset="0.5" stop-color="#c9c3bb"/>
        <stop offset="1" stop-color="#6b4a33"/>
      </linearGradient>
      <linearGradient id="exterior-tone" x1="0" y1="0" x2="1" y2="1">
        <stop offset="0" stop-color="#7fb0e0"/>
        <stop offset="0.4" stop-color="#c99a6a"/>
        <stop offset="0.8" stop-color="#5fb8c4"/>
        <stop offset="1" stop-color="#b9aa94"/>
      </linearGradient>
    </defs>
    <rect class="panel panel--left" x="45" y="0" width="266" height="630" fill="var(--charcoal)"/>
    <rect class="panel panel--contact" x="311" y="0" width="284" height="630" fill="var(--charcoal)"/>
    <line class="fold" x1="311" y1="0" x2="311" y2="630" stroke="var(--fold-line)" stroke-width="0.8"/>
    <line class="fold" x1="595" y1="0" x2="595" y2="630" stroke="var(--fold-line)" stroke-width="0.8"/>
    <polygon class="photo photo--interior" role="img" aria-label="Photo of a bright modern master bathroom with glass shower, soaking tub and wood floor"
      points="45,405 232,314 311,352 311,630 45,630" fill="url(#interior-tone)"/>
    <polygon class="photo photo--exterior" role="img" aria-label="Photo of a two-storey stucco home with a backyard pool and patio"
      points="595,0 855,0 855,183 595,327" fill="url(#exterior-tone)"/>
    <polygon class="accent accent--shadow" points="595,275 652,301 595,330" fill="var(--charcoal-dark)"/>
    <polygon class="accent accent--gold" points="595,327 855,183 855,262 595,407" fill="var(--gold)"/>
    <polygon class="accent accent--charcoal" points="855,262 855,338 775,306" fill="var(--charcoal)"/>
    <polygon class="accent accent--silver" points="775,306 855,338 855,407 708,344" fill="var(--silver)"/>
  </svg>

  <section class="contact-panel">
    <h2 class="contact-panel__title">CONTACT US</h2>
    <p class="contact-panel__web">WEBSITE |<br>www.larchviewhomeshots.com</p>
    <blockquote class="testimonial">
      <p class="testimonial__quote">I been working with Larchview Home Shots for years.<br>They are great to work with.<br>Fast turn around time and great attention to detail.</p>
      <p class="testimonial__author">Marla Whitfield<br>Summit Crest Realty</p>
    </blockquote>
    <p class="contact-panel__cta">Book now, View rates &amp; contact us online</p>
  </section>

  <section class="brand">
    <span class="brand__mark"></span>
    <p class="brand__name">Larchview Home Shots</p>
    <p class="brand__former">formerly Canyon Ridge Home Tours</p>
  </section>
</main>
</body>
</html>
```